Label design for loose leaf tea pouches and tins

Starting my loose leaf tea business and looking for product labels.
I already have logo designed and would love it to be worked into the label;
Label sizes and sample text is in the attachments;
Pouches and tins pictures are also in the attachments.

looking for the recommendation on what is the best color for the pouch.
Updates

Here is the link: https://docs.plumbrix.com/spreadsheets/d/7kTq2wLm9PzX4vHc8RnYb3JdFs6GaUe1QoWt5NyKx2Ze/edit

Adding the pdf since plumbrix links do not work here

Target Market(s)

Women and men, 35+, USA

Font styles to use
Serif

Requirements
Must have
• Front and back label

```html
<!DOCTYPE html>
<html lang="en">
<head>
<meta charset="utf-8">
<title>Steep Hollow – Tin Labels</title>
<link rel="stylesheet" href="https://fonts.googleapis.com/css2?family=Tillana:wght@600;700&family=Quattrocento:wght@400;700&display=swap">
<style>
  :root {
    --backdrop: #dcd6c8;
    --turmeric-dark: #3a1a0d;
    --turmeric-main: #f08a12;
    --cardamom-dark: #2a2926;
    --cardamom-main: #c4a227;
    --apple-dark: #1c4a1d;
    --apple-main: #dde31c;
    --ink: #1c1a17;
    --ink-soft: #4a3a22;
    --paper: #f4efe4;
  }
  * { box-sizing: border-box; margin: 0; padding: 0; }
  html, body { width: 1200px; height: 819px; overflow: hidden; }
  body {
    position: relative;
    background: var(--backdrop);
    font-family: "Quattrocento", Georgia, serif;
  }
  .label-row {
    position: absolute;
    top: 250px;
    left: 0;
    width: 1200px;
    display: flex;
    justify-content: center;
    gap: 30px;
  }
  .tin-label {
    position: relative;
    width: 310px;
    height: 320px;
    display: flex;
    flex-direction: column;
    overflow: hidden;
  }
  .tin-label.back { width: 150px; }
  .band-top { height: 70px; background: var(--dark); }
  .band-main {
    position: relative;
    height: 180px;
    background: var(--main);
    text-align: center;
    overflow: hidden;
  }
  .band-bottom {
    position: relative;
    height: 70px;
    background: var(--dark);
  }
  .ornament {
    position: absolute;
    left: 50%; top: 10px;
    width: 280px; height: 280px;
    transform: translateX(-50%);
    border-radius: 50%;
    background: radial-gradient(circle, rgba(255,255,255,0.10), rgba(255,255,255,0.02) 70%, transparent 72%);
  }
  .illustration {
    position: absolute;
    left: 50%; top: 14px;
    width: 100px; height: 54px;
    transform: translateX(-50%);
    border-radius: 8px;
    background: var(--illus);
  }
  .flavour-name {
    position: absolute;
    left: 0; right: 0; top: 76px;
    font-family: "Tillana", Georgia, serif;
    font-weight: 700;
    font-size: 30px;
    line-height: 1;
    color: var(--ink);
    white-space: nowrap;
  }
  .flavour-name.long { font-size: 24px; top: 82px; }
  .tagline {
    position: absolute;
    left: 0; right: 0; top: 116px;
    font-size: 8.5px;
    line-height: 1.2;
    color: var(--ink-soft);
  }
  .net-weight, .servings {
    position: absolute;
    top: 22px;
    font-size: 10.5px;
    font-weight: 700;
    color: var(--paper);
    line-height: 1.3;
  }
  .net-weight { left: 16px; }
  .servings { right: 14px; text-align: center; font-style: italic; }
  .brand-seal {
    position: absolute;
    left: 50%; top: 238px;
    width: 104px; height: 104px;
    transform: translateX(-50%);
    border-radius: 50%;
    background: var(--dark);
    border: 2px solid var(--paper);
    display: flex;
    align-items: flex-start;
    justify-content: center;
    padding-top: 54px;
  }
  .brand-name {
    font-family: "Quattrocento", Georgia, serif;
    font-weight: 700;
    font-size: 11px;
    letter-spacing: 1.2px;
    color: var(--paper);
    white-space: nowrap;
  }
  .back-copy {
    position: absolute;
    left: 12px; right: 12px; top: 16px;
    text-align: left;
    font-size: 8px;
    line-height: 1.35;
    color: var(--ink-soft);
  }
  .back-copy p + p { margin-top: 6px; }
  .turmeric { --dark: var(--turmeric-dark); --main: var(--turmeric-main); --illus: #a8600f; }
  .cardamom { --dark: var(--cardamom-dark); --main: var(--cardamom-main); --illus: #6e6a3c; }
  .apple    { --dark: var(--apple-dark);    --main: var(--apple-main);    --illus: #4f6a2a; }
</style>
</head>
<body>
  <main class="label-row">
    <section class="tin-label back turmeric" aria-label="Back label">
      <div class="band-top"></div>
      <div class="band-main">
        <div class="back-copy">
          <p>Ingredients: turmeric root, ginger, lemongrass, cinnamon, black pepper.</p>
          <p>Brewing: steep 1 tsp in 8 oz of hot water for 5–7 minutes.</p>
          <p>Store in a cool, dry place.</p>
        </div>
      </div>
      <div class="band-bottom"></div>
    </section>

    <section class="tin-label turmeric">
      <div class="band-top"></div>
      <div class="band-main">
        <div class="ornament" role="img" aria-label="Faint line mandala ornament"></div>
        <div class="illustration" role="img" aria-label="Engraved illustration of turmeric root"></div>
        <h2 class="flavour-name">Turmeric</h2>
        <p class="tagline">Delicious concoction of Indian herbs<br>and flowers to help you slow down<br>and unwind</p>
      </div>
      <div class="band-bottom">
        <p class="net-weight">3.4 oz / 100g</p>
        <p class="servings">50 servings<br>Decaffinate</p>
      </div>
      <div class="brand-seal"><span class="brand-name">STEEP HOLLOW</span></div>
    </section>

    <section class="tin-label cardamom">
      <div class="band-top"></div>
      <div class="band-main">
        <div class="ornament" role="img" aria-label="Faint line mandala ornament"></div>
        <div class="illustration" role="img" aria-label="Engraved illustration of a black cardamom sprig with leaves and flowers"></div>
        <h2 class="flavour-name long">Black Cardamom</h2>
        <p class="tagline">Delicious concoction of Indian herbs<br>and flowers to help you slow down<br>and unwind</p>
      </div>
      <div class="band-bottom">
        <p class="net-weight">3.4 oz / 100g</p>
        <p class="servings">50 servings<br>Decaffinate</p>
      </div>
      <div class="brand-seal"><span class="brand-name">STEEP HOLLOW</span></div>
    </section>

    <section class="tin-label apple">
      <div class="band-top"></div>
      <div class="band-main">
        <div class="ornament" role="img" aria-label="Faint line mandala ornament"></div>
        <div class="illustration" role="img" aria-label="Engraved illustration of an apple"></div>
        <h2 class="flavour-name">Apple</h2>
        <p class="tagline">Delicious concoction of Indian herbs<br>and flowers to help you slow down<br>and unwind</p>
      </div>
      <div class="band-bottom">
        <p class="net-weight">3.4 oz / 100g</p>
        <p class="servings">50 servings<br>Decaffinate</p>
      </div>
      <div class="brand-seal"><span class="brand-name">STEEP HOLLOW</span></div>
    </section>
  </main>
</body>
</html>
```